I need a poster designed for my upcoming film "The Lantern Keeper's Hour". Here is a link to the rough cut so you can get a feel for the story. The password is: fish https://reelvault.example/47186295 The synopsis: Dorian Pell and Lorna Bevrikova discover the importance of change in this character-driven drama. After their encounter at a fish store, things become more challenging when they unknowingly help each other find themselves and ignite an unlikely love-interest. Our color palette is blue, yellow, red, gold, and brown. I have attached dng. stills to use as assets if you choose to use them. The main characters don't necessarily have to be on the poster. I'm leaving the creativity up to you. All I ask is the poster matches the films aesthetic which you will easily be able to identify once you've watched the above posted link. Film credits usually are located on the bottom of movie posters. Here is the order I am looking for. A Film By Paul Ashby "The Lantern Keeper's Hour" Morgan Fealbrook, Greta Vammoni, Tavo RuvalcaƱa, Wilma Draste Production Designer Mateo Quirindo Director of Photography Simon Belcraft Executive Producer Paul Ashby Produced By Deborah Valquist Screenplay By Paul Ashby Directed By Paul Ashby. Please have the dimensions be 20x30 inches. I hope you can have fun with this project and please contact me with any questions or concerns. Thanks, Paul Ashby

```html
<!DOCTYPE html>
<html lang="en">
<head>
<meta charset="utf-8">
<title>The Lantern Keeper's Hour — Poster</title>
<link rel="stylesheet" href="https://fonts.googleapis.com/css2?family=Montserrat:wght@300;400;700&display=swap">
<style>
  :root {
    --navy: #070b35;
    --deep-blue: #0d1a8a;
    --bright-blue: #1f3fd6;
    --slate: #3a4660;
    --amber: #f2a600;
    --white: #ffffff;
    --red: #c2141c;
    --brown: #6b4a2a;
    --olive: #9cb13a;
  }
  html, body {
    margin: 0;
    padding: 0;
    width: 800px;
    height: 1200px;
    overflow: hidden;
    background: var(--navy);
  }
  .poster {
    position: relative;
    width: 800px;
    height: 1200px;
    overflow: hidden;
    font-family: "Montserrat", sans-serif;
    color: var(--white);
  }
  .key-art {
    position: absolute;
    inset: 0;
    background:
      radial-gradient(ellipse 120px 160px at 210px 140px, rgba(156,177,58,0.85), transparent 70%),
      radial-gradient(ellipse 380px 200px at 560px 110px, rgba(31,63,214,0.75), transparent 70%),
      radial-gradient(ellipse 260px 320px at 700px 560px, rgba(58,70,96,0.9), transparent 70%),
      radial-gradient(ellipse 200px 260px at 560px 420px, rgba(31,63,214,0.55), transparent 70%),
      radial-gradient(ellipse 260px 200px at 650px 1120px, rgba(194,20,28,0.85), transparent 70%),
      radial-gradient(ellipse 240px 220px at 220px 1060px, rgba(107,74,42,0.75), transparent 70%),
      radial-gradient(ellipse 200px 260px at 500px 820px, rgba(107,74,42,0.55), transparent 70%),
      linear-gradient(180deg, #0a1050 0%, var(--navy) 45%, #0b0f2e 100%);
  }
  .byline {
    position: absolute;
    top: 60px;
    left: 0;
    width: 100%;
    text-align: center;
    font-size: 21px;
    font-weight: 400;
    letter-spacing: 1px;
  }
  .byline strong { font-weight: 700; }
  .title-line {
    position: absolute;
    left: 0;
    width: 100%;
    margin: 0;
    text-align: center;
    font-weight: 300;
    font-size: 124px;
    line-height: 1;
    color: var(--amber);
    white-space: nowrap;
  }
  .title-line.l1 { top: 130px; }
  .title-line.l2 { top: 374px; }
  .title-line.l3 { top: 618px; }
  .title-line.l4 { top: 862px; }
  .cast-name {
    position: absolute;
    left: 0;
    width: 100%;
    text-align: center;
    font-size: 20px;
    font-weight: 400;
    letter-spacing: 1px;
  }
  .cast-name strong { font-weight: 700; }
  .cast-name.c1 { top: 300px; }
  .cast-name.c2 { top: 540px; }
  .cast-name.c3 { top: 784px; }
  .cast-name.c4 { top: 1020px; }
  .billing-block {
    position: absolute;
    top: 1126px;
    left: 0;
    width: 100%;
    text-align: center;
    font-size: 8px;
    line-height: 11px;
    letter-spacing: 0.3px;
    text-transform: uppercase;
  }
  .billing-block .role { font-size: 5px; margin: 0 1px 0 4px; }
</style>
</head>
<body>
  <main class="poster">
    <div class="key-art" role="img" aria-label="Blurred close-up photograph of a glass fish bowl with aquarium gravel, glowing in deep blue, amber and red light"></div>

    <div class="byline">A FILM BY <strong>PAUL ASHBY</strong></div>

    <h1 class="title-line l1">THE</h1>
    <div class="cast-name c1">MORGAN <strong>FEALBROOK</strong></div>
    <div class="title-line l2">LANTERN</div>
    <div class="cast-name c2">GRETA <strong>VAMMONI</strong></div>
    <div class="title-line l3">KEEPER'S</div>
    <div class="cast-name c3">TAVO <strong>RUVALCAÑA</strong></div>
    <div class="title-line l4">HOUR</div>
    <div class="cast-name c4">WILMA <strong>DRASTE</strong></div>

    <div class="billing-block">
      <div><span class="role">A film by</span>Paul Ashby &nbsp;"The Lantern Keeper's Hour"<span class="role">starring</span>Morgan Fealbrook &nbsp;Greta Vammoni &nbsp;Tavo Ruvalcaña &nbsp;Wilma Draste</div>
      <div><span class="role">Production designer</span>Mateo Quirindo<span class="role">Director of photography</span>Simon Belcraft<span class="role">Executive producer</span>Paul Ashby</div>
      <div><span class="role">Produced by</span>Deborah Valquist<span class="role">Screenplay by</span>Paul Ashby<span class="role">Directed by</span>Paul Ashby</div>
    </div>
  </main>
</body>
</html>
```